Kindro - Bringing Warmth and Quality to Senior Living

We are a new company based in Sydney, Australia. We have developed a state-of-the-art app for communication between aged care facilities and families.

Kindro has been developed for facilities to augment the best possible care by providing easy, safe and secure communication for families to stay in touch with their loved ones.
Updates

the website needs to be designed so we can add functionality including multilingual support. display in different languages.we also require enquiry and email/data base function. we want it simple and clean so its responsive. the target audience will be 40+ in age. there will be a video on home page. would like to start with 6 pages/ subjects -homepage -about us -our solution -demonstration page, this will be a page that contains videos of people using our product -customer testimonials -contact us

Target Market(s)

Aged care facilities.
Families (over 40’s age group) who are looking for a facility for their loved ones.

Number of Pages Required

5+ page

Font styles to use
Sans Serif

Colors
faa54b
ffffff
0255a3

Requirements
Must have
• - Our corporate colour is #EE8811.
• - If you're using stock photography, please use brimlo prints photos as we have a license for their photos.
• - The design needs to be responsive (mobile and desktop)
• -White space on each page
Nice to have
• -need to leave a place for a future animation video to be added in on the home tab
Should not have
• we don't want flash technology

```html
<!DOCTYPE html>
<html lang="en">
<head>
<meta charset="utf-8">
<title>Kindro - Bringing Warmth and Quality to Senior Living</title>
<link href="https://fonts.googleapis.com/css2?family=Noticia+Text:wght@400;700&family=Poppins:wght@800&family=Roboto:wght@400;500&display=swap" rel="stylesheet">
<style>
:root{
  --orange:#f7931e;
  --orange-soft:#faa54b;
  --navy:#0a0f2c;
  --ink:#222;
  --muted:#777;
  --light:#f3f3f3;
  --white:#fff;
}
*{box-sizing:border-box;margin:0;padding:0}
html,body{width:1200px;height:3266px;overflow:hidden}
body{position:relative;font-family:'Noticia Text',Georgia,serif;color:var(--ink);background:var(--white)}
.abs{position:absolute}
a{color:inherit;text-decoration:none}

/* header */
.site-header{position:absolute;left:0;top:0;width:1200px;height:89px;background:var(--white)}
.brand{position:absolute;left:134px;top:20px;display:flex;align-items:center;gap:10px;color:var(--orange);font-size:38px;font-weight:700}
.brand-dot{width:40px;height:40px;border-radius:50%;border:6px solid var(--orange)}
.topbar{position:absolute;right:133px;top:11px;display:flex;align-items:center;gap:14px;font-size:13px;color:#555}
.flag{width:18px;height:12px;background:linear-gradient(#b22234 0 50%,#3c3b6e 50%)}
.btn-enquire{background:var(--orange);color:#fff;font-size:11px;font-weight:700;width:142px;height:33px;display:flex;align-items:center;justify-content:center;letter-spacing:.5px;margin-left:18px}
.main-nav{position:absolute;right:135px;top:64px;display:flex;gap:18px;font-size:11px;color:#444;letter-spacing:.3px}
.main-nav .active{color:var(--orange)}

/* hero */
.hero{position:absolute;left:0;top:89px;width:1200px;height:476px;background:linear-gradient(100deg,#9ea4ae 0%,#c8c5c0 35%,#6b8fa0 65%,#b9aa98 100%)}
.hero::after{content:"";position:absolute;inset:0;background:rgba(20,30,50,.35)}
.hero-content{position:relative;z-index:1;text-align:center;color:#fff}
.hero-kicker{position:absolute;left:0;width:1200px;top:136px;font-size:28px;letter-spacing:.5px}
.hero-title{position:absolute;left:0;width:1200px;top:180px;font-family:'Poppins',Arial,sans-serif;font-weight:800;font-size:50px;letter-spacing:-1px}
.hero-text{position:absolute;left:340px;width:520px;top:255px;font-size:13px;line-height:24px}
.btn-hero{position:absolute;left:505px;top:321px;width:189px;height:52px;background:var(--orange);color:#fff;font-size:14px;font-weight:700;display:flex;align-items:center;justify-content:center}
.hero-arrow{position:absolute;top:212px;width:28px;height:28px;border:2px solid #fff;border-radius:50%;z-index:1}

/* welcome */
.welcome{position:absolute;left:0;top:565px;width:1200px;height:440px;background:var(--white);border-top-left-radius:120px}
.welcome h1{position:absolute;left:134px;top:78px;font-size:36px;font-weight:400}
.welcome h1 span{color:var(--orange)}
.welcome p{position:absolute;left:138px;width:480px;font-size:13px;line-height:24px;color:var(--muted)}
.btn-learn{position:absolute;left:137px;top:297px;width:193px;height:40px;background:var(--orange);color:#fff;font-size:13px;display:flex;align-items:center;justify-content:center}
.video-frame{position:absolute;left:657px;top:509px;width:415px;height:397px;background:var(--white);border-bottom-right-radius:110px}
.video{position:absolute;left:665px;top:516px;width:399px;height:382px;background:linear-gradient(135deg,#3c4660,#5b6070 50%,#2e3650);border-bottom-right-radius:100px}
.video-label{position:absolute;left:0;width:100%;top:254px;text-align:center;color:#fff;font-size:19px}

/* why */
.why{position:absolute;left:0;top:1005px;width:1200px;height:568px;background:var(--orange-soft);color:#fff;text-align:center}
.why h2{position:absolute;left:0;width:1200px;top:38px;font-size:34px;font-weight:400}
.why p{position:absolute;left:285px;width:630px;top:103px;font-size:13px;line-height:24px}
.circle{position:absolute;border-radius:50%;border:5px solid #fff}
.circle-label{position:absolute;font-size:15px;font-weight:700;letter-spacing:2px;width:300px;text-align:center}
.circle-info{position:absolute;inset:0;display:flex;flex-direction:column;justify-content:center;align-items:center;font-size:11px;line-height:23px;padding:0 22px}
.circle-info b{color:var(--orange);font-size:9px;margin-top:6px}

/* team */
.team{position:absolute;left:0;top:1573px;width:1200px;height:586px;text-align:center}
.team h2{position:absolute;left:0;width:1200px;top:52px;font-size:36px;font-weight:400}
.team p{position:absolute;left:410px;width:380px;top:114px;font-size:12px;line-height:24px;color:var(--muted)}
.member{position:absolute;top:193px;width:208px;height:238px}
.member .photo{width:100%;height:100%;border-radius:6px}
.member .name{position:absolute;left:26px;top:217px;width:152px;height:43px;background:var(--orange);color:#fff;border-radius:22px;display:flex;align-items:center;justify-content:center;font-size:14px;font-weight:700}
.dots{position:absolute;left:574px;top:2090px;display:flex;gap:19px}
.dots i{width:10px;height:10px;border-radius:50%;background:#ccc;display:block}
.dots i.on{background:var(--orange)}

/* testimonials */
.testimonials{position:absolute;left:0;top:2159px;width:1200px;height:511px;background:var(--light)}
.testimonials h2{position:absolute;left:0;width:1200px;top:52px;text-align:center;font-size:34px;font-weight:400}
.quote-card{position:absolute;top:142px;width:285px;height:290px;background:#fff}
.quote-card p{position:absolute;left:46px;top:34px;width:210px;font-size:14px;line-height:29px;color:var(--muted)}
.avatar{position:absolute;left:34px;top:200px;width:55px;height:55px;border-radius:50%;background:linear-gradient(#d5cfc8,#9a948f)}
.author{position:absolute;left:107px;top:206px;font-size:14px}
.author small{display:block;font-size:11px;color:#999;margin-top:6px}
.quote-mark{position:absolute;right:6px;bottom:-4px;font-size:110px;line-height:1;color:var(--orange-soft);opacity:.75;font-family:Georgia,serif;height:60px;overflow:hidden}
.quote-tail{position:absolute;left:90px;bottom:-14px;width:0;height:0;border-left:30px solid #fff;border-bottom:14px solid transparent}

/* enquiry */
.enquiry{position:absolute;left:0;top:2670px;width:1200px;height:311px;background:linear-gradient(90deg,#f39a2e,#f6a53f)}
.enquiry h2{position:absolute;left:0;width:1200px;top:42px;text-align:center;color:#fff;font-size:32px;font-weight:400}
.field{position:absolute;height:40px;background:#fff;font-size:10px;color:#aaa;padding-left:23px;display:flex;align-items:center}
.btn-send{position:absolute;left:729px;top:190px;width:234px;height:40px;background:var(--navy);color:#fff;font-size:11px;font-weight:700;display:flex;align-items:center;justify-content:center;letter-spacing:.5px}
.curve{position:absolute;left:0;top:2600px}
.to-top{position:absolute;left:1080px;top:2852px;width:50px;height:50px;border-radius:50%;background:var(--orange);border:3px solid #fff;display:flex;align-items:center;justify-content:center}

/* footer */
.site-footer{position:absolute;left:0;top:2981px;width:1200px;height:285px;background:var(--navy);color:#fff}
.f-col{position:absolute;top:97px}
.f-col h4{font-size:12px;color:var(--orange);font-weight:700;letter-spacing:.3px;margin-bottom:12px}
.f-row{display:flex;align-items:center;gap:14px;font-size:12px;line-height:20px}
.f-row.sans{font-family:'Roboto',Arial,sans-serif;font-size:14px}
.social{display:flex;gap:13px;margin-top:6px}
.social i{width:20px;height:20px;display:block}
.copyright{position:absolute;left:0;width:1200px;top:222px;text-align:center;font-family:'Roboto',Arial,sans-serif;font-size:10px}
</style>
</head>
<body>

<header class="site-header">
  <div class="brand"><span class="brand-dot"></span>Kindro</div>
  <div class="topbar">
    <span class="flag" role="img" aria-label="Language selector flag"></span>
    <svg width="14" height="14" viewBox="0 0 24 24"><path d="M6.6 10.8a15.1 15.1 0 006.6 6.6l2.2-2.2c.3-.3.7-.4 1-.2 1.1.4 2.3.6 3.6.6.6 0 1 .4 1 1V20c0 .6-.4 1-1 1A17 17 0 013 4c0-.6.4-1 1-1h3.5c.6 0 1 .4 1 1 0 1.3.2 2.5.6 3.6.1.3 0 .7-.2 1z" fill="#999"/></svg>
    <span>Callnow:&nbsp; 5310 2284</span>
    <a class="btn-enquire" href="#enquiry">ENQUIRE NOW</a>
  </div>
  <nav class="main-nav">
    <a class="active" href="#">HOME</a><a href="#">ABOUT US</a><a href="#">OUR SOLUTION</a><a href="#">DEMONSTRATION</a><a href="#">TESTIMONIALS</a><a href="#">CONTACT US</a>
  </nav>
</header>

<section class="hero" role="img" aria-label="Photo of a carer serving a meal to a smiling elderly woman">
  <div class="hero-content">
    <div class="hero-kicker">HELP THE ELDERLY PEOPLE</div>
    <div class="hero-title">WORLD'S BEST SENIOR CARE</div>
    <p class="hero-text">We provides always our best services for our clients and &nbsp;always try to achieve our client's trust and satisfaction.</p>
    <a class="btn-hero" href="#">View Details</a>
  </div>
  <svg class="hero-arrow" style="left:96px" viewBox="0 0 28 28"><path d="M16 8l-6 6 6 6" stroke="#fff" stroke-width="2.5" fill="none"/></svg>
  <svg class="hero-arrow" style="left:1088px" viewBox="0 0 28 28"><path d="M12 8l6 6-6 6" stroke="#fff" stroke-width="2.5" fill="none"/></svg>
</section>

<section class="welcome">
  <h1>Welcome to <span>Kindro</span></h1>
  <p style="top:135px">Kindro is a state-of-the-art solution that provides communication between aged care facilities, residents and families.</p>
  <p style="top:201px">Kindro has been developed for facilities to augment the best possible care by providing easy, safe and secure communication for families to stay in touch withtheir loved ones.</p>
  <a class="btn-learn" href="#">Learn more about Kindro</a>
</section>

<div class="video-frame"></div>
<div class="video" role="img" aria-label="Video still of elderly residents sharing fruit at a table">
  <svg class="abs" style="left:166px;top:22px;top:22px" width="0" height="0"></svg>
  <svg class="abs" style="left:165px;top:122px" width="70" height="70" viewBox="0 0 70 70"><circle cx="35" cy="35" r="32" stroke="#fff" stroke-width="4" fill="none"/><path d="M27 21l22 14-22 14z" fill="#fff"/></svg>
  <div class="video-label">Watch Our Video</div>
</div>

<section class="why">
  <h2>Why Kindro?</h2>
  <p>With the spotlight on aged care, facilities need every advantaged to demonstrate excellence to residents and their families, and Kindro provide a solution. Reports have been so confronting within the industry that a Royal Commission into Aged Care Quality and Safety was created by the Federal Government.</p>
  <svg class="abs" style="left:0;top:300px" width="1200" height="140" viewBox="0 0 1200 140"><path d="M0 72 Q 90 95 170 95 M392 88 Q 450 75 490 70 M725 68 Q 780 72 825 60 M1058 95 Q 1130 110 1200 140" stroke="#fff" stroke-width="1.5" stroke-dasharray="10 6" fill="none" opacity=".8"/></svg>
  <div class="circle" style="left:167px;top:259px;width:224px;height:224px;background:#1f2440">
    <div class="circle-info">Offers families proof of excellent care.Competitive advantages over other facilities.<b>MORE INFO</b></div>
  </div>
  <div class="circle-label" style="left:134px;top:510px">FACILITIES</div>
  <div class="circle" role="img" aria-label="Photo of seniors exercising with resistance bands" style="left:488px;top:213px;width:236px;height:236px;background:linear-gradient(135deg,#a9b39a,#d6c6a8,#8aa7a0)"></div>
  <div class="circle-label" style="left:464px;top:470px">FAMILIES</div>
  <div class="circle" role="img" aria-label="Photo of smiling elderly couple giving thumbs up" style="left:821px;top:253px;width:236px;height:236px;background:linear-gradient(135deg,#d4c7bb,#b6a79b,#e2d6c8)"></div>
  <div class="circle-label" style="left:795px;top:504px">RESIDENTS CARE</div>
</section>

<section class="team">
  <h2>Our Team</h2>
  <p>Lorem ipsum dolor sit amet, consectetur adipisicing elit. Rem autem voluptatem obcaecati!</p>
  <div class="member" style="left:134px"><div class="photo" role="img" aria-label="Portrait of team member in a blue blazer" style="background:linear-gradient(#6d8a4e,#2c3d5a)"></div><div class="name">Martin Hale</div></div>
  <div class="member" style="left:369px"><div class="photo" role="img" aria-label="Portrait of team member in a light shirt" style="background:linear-gradient(#9fb1c0,#c7a88d)"></div><div class="name">Owen Pryce</div></div>
  <div class="member" style="left:615px"><div class="photo" role="img" aria-label="Portrait of team member against a pink wall" style="background:linear-gradient(#c2405a,#7d90b0)"></div><div class="name">Clara Voss</div></div>
  <div class="member" style="left:859px"><div class="photo" role="img" aria-label="Portrait of team member in a striped shirt" style="background:linear-gradient(#b8b2aa,#8aa0c2)"></div><div class="name">Nina Marsh</div></div>
</section>
<div class="dots"><i></i><i class="on"></i><i></i></div>

<section class="testimonials">
  <h2>Some of our Awesome Testimonials</h2>
  <div class="quote-card" style="left:134px">
    <p>Harbor Lend is a wonderful place with highly experienced experts! With their help I bought my first apartment and I'm happy now!</p>
    <div class="avatar" role="img" aria-label="Client portrait"></div>
    <div class="author">Ruth Ellory<small>Accountant</small></div>
    <div class="quote-mark">&ldquo;</div><div class="quote-tail"></div>
  </div>
  <div class="quote-card" style="left:462px">
    <p>Harbor Lend is a wonderful place with highly experienced experts! With their help I bought my first apartment and I'm happy now!</p>
    <div class="avatar" role="img" aria-label="Client portrait"></div>
    <div class="author">Simon Tarrant<small>Accountant</small></div>
    <div class="quote-mark">&ldquo;</div><div class="quote-tail"></div>
  </div>
  <div class="quote-card" style="left:781px">
    <p>Harbor Lend is a wonderful place with highly experienced experts! With their help I bought my first apartment and I'm happy now!</p>
    <div class="avatar" role="img" aria-label="Client portrait"></div>
    <div class="author">Leah Moreno<small>Accountant</small></div>
    <div class="quote-mark">&ldquo;</div><div class="quote-tail"></div>
  </div>
</section>

<section class="enquiry" id="enquiry" role="img" aria-label="Orange-tinted photo of a cheerful crowd">
  <h2>Enquiry Now</h2>
  <div class="field" style="left:228px;top:128px;width:234px">Name</div>
  <div class="field" style="left:478px;top:128px;width:234px">Email Address</div>
  <div class="field" style="left:729px;top:128px;width:234px">Phone Number</div>
  <div class="field" style="left:228px;top:190px;width:484px">Message</div>
  <div class="btn-send">SEND NOW</div>
</section>

<svg class="curve" width="1200" height="390" viewBox="0 0 1200 390">
  <path d="M1200 20 C 1170 200 1080 370 860 380 L 0 382 L 0 390 L 1200 390 Z" fill="#0a0f2c"/>
  <path d="M1198 0 C 1170 190 1080 368 860 378 L 0 380" stroke="#fff" stroke-width="6" fill="none"/>
</svg>

<div class="to-top"><svg width="18" height="18" viewBox="0 0 18 18"><path d="M4 11l5-5 5 5" stroke="#fff" stroke-width="2" fill="none"/></svg></div>

<footer class="site-footer">
  <div class="f-col" style="left:167px">
    <h4>ADDRESS</h4>
    <div class="f-row">
      <svg width="18" height="22" viewBox="0 0 18 22"><path d="M9 1a7 7 0 017 7c0 5-7 13-7 13S2 13 2 8a7 7 0 017-7z" stroke="#f7931e" stroke-width="1.5" fill="none"/><circle cx="9" cy="8" r="2.5" stroke="#f7931e" stroke-width="1.5" fill="none"/></svg>
      <span>18 Larkfield Row, Suite 4B,<br>Maplewood, NS 2417</span>
    </div>
  </div>
  <div class="f-col" style="left:472px">
    <h4>PHONE NUMBER</h4>
    <div class="f-row sans" style="margin-top:14px">
      <svg width="20" height="20" viewBox="0 0 24 24"><path d="M6.6 10.8a15.1 15.1 0 006.6 6.6l2.2-2.2c.3-.3.7-.4 1-.2 1.1.4 2.3.6 3.6.6.6 0 1 .4 1 1V20c0 .6-.4 1-1 1A17 17 0 013 4c0-.6.4-1 1-1h3.5c.6 0 1 .4 1 1 0 1.3.2 2.5.6 3.6.1.3 0 .7-.2 1z" stroke="#f7931e" stroke-width="1.5" fill="none"/></svg>
      <span>(02) 7410 5528</span>
    </div>
  </div>
  <div class="f-col" style="left:701px">
    <h4>MAIL ADDRESS</h4>
    <div class="f-row sans" style="margin-top:10px">
      <svg width="20" height="16" viewBox="0 0 20 16"><rect x="1" y="1" width="18" height="14" stroke="#f7931e" stroke-width="1.5" fill="none"/><path d="M1 1l9 8 9-8" stroke="#f7931e" stroke-width="1.5" fill="none"/></svg>
      <span>hello@kindro.example</span>
    </div>
  </div>
  <div class="f-col" style="left:917px">
    <h4>SOCIAL LINKS</h4>
    <div class="social"><i style="background:#3a9ad9"></i><i style="background:#3b5998"></i><i style="background:#d9453a"></i></div>
  </div>
  <div class="copyright">2018 &copy; kindro.example. All Rights Reserved</div>
</footer>

</body>
</html>
```